Hello,
Corinne Haskett Equestrian needs a business card. We are a high performance show jumping stables based at Willowmere Reserve in morningotn. We pride ourselves on producing high quality show jumping horses and competing our stock at a high level. My business card need to have my logo on it, and i would like it to have a classic design with a modern touch. I would like it to have quite a natural feel about it. It needs to be in a font which is easy to read as I spend a lot of time competing internationally and overseas, and i need to be able to give it out to breeders and contacts where English isnt their first language. I will need it to include the following details:
-Corinne Haskett Equestrian
-Based at Willowmere Reserve Mornington
-Address: 17 Tremont Lane Mornington Victoria 3931
-Mobile number: 0412605948
- website: www.corinnehaskettequestrian.example
Target Market(s)
For business adults who english may not be their first language
Industry/Entity Type
Business

```html
<!DOCTYPE html>
<html lang="en">
<head>
<meta charset="utf-8">
<title>Corinne Haskett Equestrian – Business Card</title>
<link rel="stylesheet" href="https://fonts.googleapis.com/css2?family=Marcellus&family=Open+Sans:wght@400&display=swap">
<style>
  :root {
    --stage: #e9e7e4;
    --card-light-center: #ffffff;
    --card-light-mid: #c9d3dc;
    --card-light-edge: #8fa1b1;
    --card-dark: #0a0b3f;
    --ink: #1f2326;
    --accent: #c2561a;
    --white: #ffffff;
  }
  * { margin: 0; padding: 0; box-sizing: border-box; }
  html, body {
    width: 1200px;
    height: 456px;
    overflow: hidden;
    background: var(--stage);
  }
  .sheet {
    position: relative;
    width: 1200px;
    height: 456px;
    display: flex;
    align-items: center;
    justify-content: center;
    gap: 60px;
  }
  .card {
    position: relative;
    width: 520px;
    height: 300px;
    box-shadow: 0 6px 18px rgba(0,0,0,0.28);
  }
  .card--front {
    background: radial-gradient(ellipse at 58% 50%, var(--card-light-center) 0%, var(--card-light-mid) 45%, var(--card-light-edge) 100%);
  }
  .card--back {
    background: var(--card-dark);
  }
  .brand {
    position: absolute;
    left: 0;
    right: 0;
    display: flex;
    flex-direction: column;
    align-items: center;
  }
  .brand__dot {
    border-radius: 50%;
    background: var(--accent);
  }
  .brand__name {
    font-family: "Marcellus", serif;
    font-weight: 400;
    white-space: nowrap;
    letter-spacing: 0.5px;
  }
  .card--front .brand { top: 34px; }
  .card--front .brand__dot { width: 46px; height: 46px; margin-bottom: 18px; }
  .card--front .brand__name { font-size: 25px; color: var(--ink); }
  .card--back .brand { top: 84px; }
  .card--back .brand__dot { width: 62px; height: 62px; margin-bottom: 26px; }
  .card--back .brand__name { font-size: 30px; color: var(--white); }
  .contact {
    position: absolute;
    left: 110px;
    top: 158px;
    font-family: "Open Sans", sans-serif;
    font-size: 13.5px;
    line-height: 18px;
    color: var(--ink);
    list-style: none;
  }
  .contact__item {
    display: flex;
    align-items: flex-start;
    gap: 6px;
    margin-bottom: 12px;
  }
  .contact__item--phone { padding-left: 90px; }
  .contact__item--web { padding-left: 40px; }
  .contact__icon {
    flex: none;
    width: 13px;
    height: 13px;
    margin-top: 2px;
    fill: var(--accent);
  }
</style>
</head>
<body>
<main class="sheet">
  <section class="card card--front" aria-label="Card front">
    <div class="brand">
      <span class="brand__dot"></span>
      <h1 class="brand__name">Corinne Haskett Equestrian</h1>
    </div>
    <ul class="contact">
      <li class="contact__item contact__item--address">
        <svg class="contact__icon" viewBox="0 0 12 12" aria-hidden="true"><path d="M6 0a4 4 0 0 0-4 4c0 3 4 8 4 8s4-5 4-8a4 4 0 0 0-4-4zm0 5.6A1.6 1.6 0 1 1 6 2.4a1.6 1.6 0 0 1 0 3.2z"/></svg>
        <span>17 Tremont Lane Mornington Victoria 3931<br>Based at Willowmere Reserve Mornington</span>
      </li>
      <li class="contact__item contact__item--phone">
        <svg class="contact__icon" viewBox="0 0 12 12" aria-hidden="true"><circle cx="6" cy="6" r="6"/><path d="M4 3.2l1 1.2-.6.8c.4.9 1 1.5 1.9 1.9l.8-.6 1.2 1-.6 1.1c-2.4-.3-4.2-2.1-4.5-4.5z" fill="#fff"/></svg>
        <span>041-260-5948</span>
      </li>
      <li class="contact__item contact__item--web">
        <svg class="contact__icon" viewBox="0 0 12 12" aria-hidden="true"><circle cx="6" cy="6" r="6"/><path d="M0.5 6h11M6 0.5v11M2 3h8M2 9h8" stroke="#fff" stroke-width="0.7" fill="none"/><ellipse cx="6" cy="6" rx="2.6" ry="5.5" stroke="#fff" stroke-width="0.7" fill="none"/></svg>
        <span>www.corinnehaskettequestrian.example</span>
      </li>
    </ul>
  </section>
  <section class="card card--back" aria-label="Card back">
    <div class="brand">
      <span class="brand__dot"></span>
      <p class="brand__name">Corinne Haskett Equestrian</p>
    </div>
  </section>
</main>
</body>
</html>
```